design an extra page for our profile

we are looking for someone to create another page like the attached but with the below changes:
heading changed to (Construction)
icons changed and names to reflect new services i.e
- Residential Building
- Commercial Building
- Landscaping
- Concrete
- Painting

the very bottom of the page is to stay the same with our office info

```html
<!DOCTYPE html>
<html lang="en">
<head>
<meta charset="utf-8">
<title>Vero Services – Construction</title>
<link rel="stylesheet" href="https://fonts.googleapis.com/css2?family=Montserrat:wght@400;500;600;700;800&family=Work+Sans:wght@500;600&display=swap">
<style>
  :root {
    --navy: #22399a;
    --accent: #3f63c8;
    --ink: #1f1f24;
    --heading-light: #262a36;
    --rule: #c9ccd3;
    --page: #ffffff;
    --backdrop: #f1f1f1;
    --photo-top: #ffffff;
    --photo-mid: #e4e7ec;
    --photo-low: #b9bec7;
  }
  * { box-sizing: border-box; margin: 0; padding: 0; }
  html, body { width: 783px; height: 1200px; overflow: hidden; background: var(--backdrop); }
  .flyer {
    position: relative; width: 783px; height: 1200px; background: var(--page);
    font-family: "Montserrat", sans-serif; color: var(--ink);
  }
  .office-photo {
    position: absolute; left: 0; top: 500px; width: 783px; height: 550px;
    background: linear-gradient(180deg, var(--photo-top) 0%, var(--photo-mid) 30%, #cfd4dc 55%, #d9dce1 78%, var(--photo-low) 100%);
  }
  .brand {
    position: absolute; top: 84px; left: 0; width: 100%; text-align: center;
    font-weight: 700; font-size: 50px; line-height: 64px;
    color: var(--navy); letter-spacing: 1px;
  }
  .headline {
    position: absolute; top: 204px; left: 0; width: 100%; text-align: center;
    font-size: 43px; line-height: 44px; color: var(--navy); letter-spacing: 0.5px;
  }
  .headline strong { font-weight: 800; }
  .headline span { font-weight: 400; color: var(--heading-light); }
  .intro {
    position: absolute; top: 255px; left: 104px; width: 575px; text-align: center;
    font-family: "Work Sans", sans-serif; font-weight: 600; font-size: 16.5px; line-height: 22.5px;
  }
  .intro em { font-style: normal; color: var(--navy); }
  .divider { position: absolute; top: 349px; left: 134px; width: 514px; height: 1px; background: var(--rule); }
  .divider::after {
    content: ""; position: absolute; left: 230px; top: -2px; width: 54px; height: 5px;
    border-radius: 3px; background: var(--accent);
  }
  .sep { position: absolute; width: 1px; background: linear-gradient(180deg, transparent, #9ea3ad 20%, #9ea3ad 80%, transparent); }
  .service { position: absolute; width: 180px; margin-left: -90px; text-align: center; }
  .service-icon { display: block; width: 78px; height: 78px; margin: 0 auto 15px; }
  .service-name {
    font-family: "Work Sans", sans-serif; font-weight: 600; font-size: 20px; line-height: 25px; color: var(--heading-light);
  }
  .contact-band {
    position: absolute; left: 0; top: 1057px; width: 783px; height: 143px; background: var(--navy);
    color: #fff; font-weight: 600; font-size: 15.5px;
  }
  .contact-row { position: absolute; left: 0; width: 100%; display: flex; justify-content: center; align-items: center; }
  .contact-row.first { top: 36px; }
  .contact-row.second { top: 74px; }
  .contact-item { display: flex; align-items: center; gap: 7px; }
  .contact-item svg { width: 14px; height: 14px; }
  .bar { width: 1px; height: 16px; margin: 0 16px; border-left: 1px dashed rgba(255,255,255,.7); }
</style>
</head>
<body>
<main class="flyer">
  <div class="office-photo" role="img" aria-label="Bright open-plan office with white desks, black chairs and city windows"></div>

  <div class="brand">VERO</div>

  <h1 class="headline"><strong>CONSTRUCTION</strong> <span>SERVICES</span></h1>
  <p class="intro">As New Tenants To The Building And As A Way Of Introducing Ourselves We Would Like <em>To Offer A 10% Discount</em> On Any Of The Below Services.</p>

  <div class="divider"></div>

  <div class="sep" style="left:283px;top:378px;height:151px"></div>
  <div class="sep" style="left:496px;top:378px;height:151px"></div>
  <div class="sep" style="left:391px;top:539px;height:147px"></div>

  <svg width="0" height="0" style="position:absolute">
    <defs>
      <g id="ring">
        <circle cx="38" cy="38" r="36" fill="none" stroke="#6b7080" stroke-width="1" stroke-dasharray="1.5 2.5"/>
        <circle cx="38" cy="38" r="31" fill="#fff" stroke="#22399a" stroke-width="5"/>
      </g>
    </defs>
  </svg>

  <div class="service" style="left:170px;top:379px">
    <svg class="service-icon" viewBox="0 0 76 76"><use href="#ring"/>
      <g fill="none" stroke="#22399a" stroke-width="1.8"><rect x="29" y="26" width="18" height="24"/><path d="M26 50h24M33 31h3M40 31h3M33 36h3M40 36h3M33 41h3M40 41h3M36 50v-5h4v5"/></g>
    </svg>
    <div class="service-name">Residential<br>Building</div>
  </div>

  <div class="service" style="left:392px;top:379px">
    <svg class="service-icon" viewBox="0 0 76 76"><use href="#ring"/>
      <g fill="none" stroke="#22399a" stroke-width="1.8"><rect x="28" y="24" width="20" height="27"/><rect x="32" y="29" width="4" height="4"/><rect x="40" y="29" width="4" height="4"/><rect x="32" y="37" width="4" height="4"/><rect x="40" y="37" width="4" height="4"/><path d="M35 51v-5h6v5"/></g>
    </svg>
    <div class="service-name">Commercial<br>Building</div>
  </div>

  <div class="service" style="left:607px;top:379px">
    <svg class="service-icon" viewBox="0 0 76 76"><use href="#ring"/>
      <g fill="none" stroke="#22399a" stroke-width="1.8"><circle cx="36" cy="32" r="7"/><path d="M36 39v11M26 50h26M44 50v-8l4-4 4 4v8M28 50c0-4 2-6 4-6"/></g>
    </svg>
    <div class="service-name">Landscaping</div>
  </div>

  <div class="service" style="left:286px;top:548px">
    <svg class="service-icon" viewBox="0 0 76 76"><use href="#ring"/>
      <g fill="none" stroke="#22399a" stroke-width="1.8"><path d="M25 45h26v-8l-5-5h-6v13"/><ellipse cx="32" cy="36" rx="7" ry="5" transform="rotate(-20 32 36)"/><circle cx="30" cy="47" r="3"/><circle cx="46" cy="47" r="3"/></g>
    </svg>
    <div class="service-name">Concrete</div>
  </div>

  <div class="service" style="left:492px;top:548px">
    <svg class="service-icon" viewBox="0 0 76 76"><use href="#ring"/>
      <g fill="none" stroke="#22399a" stroke-width="1.8"><rect x="27" y="37" width="13" height="14" rx="1"/><path d="M27 40h13M36 35l10-10 5 5-10 10zM41 40l-3 3"/></g>
    </svg>
    <div class="service-name">Painting</div>
  </div>

  <footer class="contact-band">
    <div class="contact-row first">
      <div class="contact-item">
        <svg viewBox="0 0 14 14"><path d="M3 1.5l2 2.5-1.2 1.5c.8 1.7 2 2.9 3.7 3.7L9 8l2.5 2-1 2c-4.5-.3-8.2-4-8.5-8.5z" fill="none" stroke="#fff" stroke-width="1.2"/></svg>
        HOME OFFICE: 1300987654
      </div>
      <span class="bar"></span>
      <div class="contact-item">
        <svg viewBox="0 0 14 14"><path d="M7 13s-4-4.5-4-7.5a4 4 0 018 0C11 8.5 7 13 7 13z" fill="none" stroke="#fff" stroke-width="1.4"/><circle cx="7" cy="5.5" r="1.4" fill="#fff"/></svg>
        Suite 2.04, 18 Harbour Lane Parkside
      </div>
    </div>
    <div class="contact-row second">
      <div class="contact-item">
        <svg viewBox="0 0 14 14"><g fill="none" stroke="#fff" stroke-width="1.1"><circle cx="7" cy="7" r="5.5"/><ellipse cx="7" cy="7" rx="2.4" ry="5.5"/><path d="M1.5 7h11M2.5 4h9M2.5 10h9"/></g></svg>
        WWW.VERO-SERVICES.COM.AU
      </div>
      <span class="bar"></span>
      <div class="contact-item">Sydney | Canberra | Brisbane | Melbourne</div>
    </div>
  </footer>
</main>
</body>
</html>
```